brindlecove.com website design (promote tax and financial services)

I need web design layouts for a 4-6 page website for a finance and tax services business.

Assumptions:
-Responsive design for desktop, laptop, tablet and mobile
-website will not be programmed with any flash elements
-Animation is welcomed
-stock photography may be required (royalty free preferred)
-Prefer to stay away from designs with large images that result in long loading times
-Web design will be pulled through to other digital and print promotional materials that the company develops

The audience is primarily male. Attached is the site and content map, including the company logo

Target Market(s)

individuals and small-to-medium business owners
Primary geographic market = NYC metropolitan area
Secondary geographic market = East Coast USA
Tertiary geographic market = National USA

Any stock photography should represent a diverse population

Industry/Entity Type

Financial Service

Number of Pages Required

5+ page

Font styles to use
Sans Serif

Colors
0758a4
9bcb3b

Requirements
Must have
• -Responsive design that translates nicely to mobile and tablet devices
• -Simple, clean but yet sophisticated design
• -Be in alignment with or a derivative of the logo design (provided with PPT attachment)
• -Compatibility with website programming and coding software
• -Include a countdown to the tax deadline (April 18, 2016)
• -Web-friendly fonts
• -Search box
• -Link to social media properties (via social icons)
• -Include company phone number and clickable link to activate ability to contact company by email
Nice to have
• -Simple animation, as long as it does not impact load time
• -Engaging call-to-action buttons
• -Rotating homepage banners
• -Original icons
• -"About Us" page should have a friendlier, welcoming design
• -Image/Photo caption examples
• -Assume that copy (text) can be minimized to accommodate more visual displays
• -"Continue reading" or "read more" links to expand truncated copy are welcomed
• -A pricing table (not a priority, but nice to have)
Should not have
• Overcrowded design (don't be afraid of white space, if needed)
• too many bells and whistles (flash animation, moving cursors etc.)

```html
<!DOCTYPE html>
<html lang="en">
<head>
<meta charset="utf-8">
<title>brindlecove.com — Financial Planning</title>
<link href="https://fonts.googleapis.com/css2?family=Merriweather:wght@300;400;700&family=Lato:wght@400;700&display=swap" rel="stylesheet">
<style>
:root{
  --navy:#083f7c;
  --green:#149b4a;
  --ink:#2b2b2b;
  --grey:#6b6b6b;
  --rule:#dcdcdc;
  --mist:#eeeeee;
  --dark:#343434;
  --darker:#2a2a2a;
  --white:#ffffff;
}
*{margin:0;padding:0;box-sizing:border-box}
html,body{width:1200px;height:4206px;overflow:hidden}
body{position:relative;background:var(--white);font-family:"Lato",Arial,sans-serif;color:var(--ink)}
.abs{position:absolute}
.serif{font-family:"Merriweather",Georgia,serif}
.pill{display:flex;align-items:center;justify-content:center;background:var(--green);color:var(--white);border-radius:24px;font-weight:700;text-decoration:none}

/* hero */
.hero{left:0;top:0;width:1200px;height:865px}
.hero-photo{left:334px;top:0;width:866px;height:865px;background:linear-gradient(120deg,#4b5560 0%,#8d98a3 35%,#c9d0d6 60%,#5f6b77 100%)}
.hero-panel{left:0;top:0;width:334px;height:865px;background:var(--navy)}
.social{left:50px;top:22px;display:flex;gap:12px}
.social span{width:14px;height:14px;background:var(--white);border-radius:2px;opacity:.9}
.phone{left:1010px;top:20px;color:var(--white);font-size:15px;font-weight:700;display:flex;align-items:center;gap:8px}
.brand{left:50px;top:80px;display:flex;align-items:center;gap:12px;color:var(--white);font-family:"Merriweather",Georgia,serif;font-size:24px;font-weight:400}
.brand i{width:22px;height:22px;background:var(--white);display:block}
.nav{left:373px;top:92px;display:flex;gap:30px;font-size:15px;color:var(--white)}
.nav a{color:var(--white);text-decoration:none}
.nav .current{border-bottom:2px solid var(--white);padding-bottom:6px}
.cta-top{left:995px;top:80px;width:155px;height:44px;font-size:14px}
.hero-title{left:50px;top:262px;width:270px;color:var(--white);font-size:29px;line-height:40px;font-weight:700}
.hero-lead{left:50px;top:412px;width:260px;color:var(--white);font-family:"Merriweather",Georgia,serif;font-size:16px;line-height:24px}
.hero-text{left:50px;top:500px;width:265px;color:var(--white);font-size:14px;line-height:21px;text-align:justify}

/* services */
.service{top:945px;width:330px}
.service .rule{position:absolute;left:0;top:18px;width:80px;height:1px;background:var(--rule)}
.service h3{position:absolute;left:96px;top:0;font-family:"Merriweather",Georgia,serif;font-weight:400;font-size:23px;color:var(--navy);white-space:nowrap}
.service p{position:absolute;left:96px;top:50px;width:285px;font-size:14px;line-height:21px;color:var(--grey)}
.service .pill{position:absolute;left:96px;top:200px;width:122px;height:44px;font-size:12px;letter-spacing:.5px}
.divider{left:0;width:1200px;height:1px;background:var(--rule)}

/* about */
.about-title{left:50px;top:1425px;font-size:38px;font-weight:400;color:var(--navy)}
.about-intro{left:50px;top:1525px;width:340px;font-family:"Merriweather",Georgia,serif;font-size:16px;line-height:25px;color:var(--ink)}
.about-text{left:50px;top:1628px;width:360px;font-size:14px;line-height:21px;color:var(--grey)}
.explore{left:50px;top:1778px;font-size:12px;font-weight:700;letter-spacing:1px;color:var(--ink)}
.frame-back{left:520px;top:1402px;width:442px;height:334px;border:4px solid var(--navy);background:linear-gradient(135deg,#e2e5ea,#9aa3ad)}
.frame-front{left:708px;top:1463px;width:452px;height:372px;border:4px solid var(--green);background:var(--white);padding:6px}
.frame-front div{width:100%;height:100%;background:linear-gradient(135deg,#8c7a6a,#c9bfb4 55%,#5e5a58)}

/* testimonials */
.testi-title{left:50px;top:2045px;font-size:40px;font-weight:400;color:var(--navy)}
.testi-sub{left:375px;top:2050px;width:420px;font-family:"Merriweather",Georgia,serif;font-size:15px;line-height:23px}
.arrows{left:1080px;top:2058px;display:flex;gap:24px}
.quote{top:2165px;width:350px;height:235px;border-left:1px solid var(--rule)}
.quote .mark{position:absolute;left:22px;top:0;font-family:"Merriweather",Georgia,serif;font-size:30px;color:#c8c8c8;line-height:1}
.quote p{position:absolute;left:60px;top:0;width:275px;font-size:14px;line-height:21px;color:var(--grey)}
.quote .who{position:absolute;left:60px;top:190px;font-size:13px;font-weight:700;color:var(--ink)}
.quote .role{position:absolute;left:60px;top:210px;font-size:12px;color:var(--grey)}

/* philosophy */
.band{left:0;top:2900px;width:1200px;height:665px;background:var(--mist)}
.philo-title{left:0;top:2598px;width:1200px;text-align:center;font-size:40px;font-weight:400;color:var(--navy)}
.video{left:187px;top:2700px;width:826px;height:468px;background:linear-gradient(135deg,#b8b2a8,#e6e2dc 50%,#8f8a84)}
.play{left:578px;top:2911px}
.philo-lead{left:225px;top:3205px;width:760px;font-family:"Merriweather",Georgia,serif;font-size:16px;line-height:25px;color:var(--ink)}
.philo-lead span{color:var(--grey)}
.philo-text{left:225px;top:3283px;width:760px;font-size:14px;line-height:21px;color:var(--grey)}
.cta-analysis{left:460px;top:3404px;width:280px;height:46px;font-size:15px}

/* signup & contact */
.connect{left:0;top:3565px;width:1200px;height:335px;background:var(--dark)}
.block-title{font-family:"Merriweather",Georgia,serif;font-size:36px;color:var(--white);font-weight:400}
.signup-note{left:50px;top:3700px;width:330px;font-size:15px;line-height:21px;font-weight:700;color:var(--white)}
.email-field{left:50px;top:3768px;width:308px;height:42px;border-radius:21px;background:var(--white);color:#9a9a9a;font-size:13px;padding:12px 18px}
.submit{left:368px;top:3768px;width:122px;height:42px;font-size:14px}
.contact-row{left:614px;display:flex;font-size:14px}
.contact-row dt{width:92px;color:#9a9a9a}
.contact-row dd{color:var(--white);font-weight:700}

/* footer */
.footer{left:0;top:3900px;width:1200px;height:306px;background:var(--darker)}
.fine{left:50px;top:3950px;width:410px;font-size:10px;line-height:15px;color:#8f8f8f}
.fine p+p{margin-top:10px}
.copyright{left:50px;top:4135px;font-size:10px;letter-spacing:1px;color:#8f8f8f}
.foot-col h4{font-family:"Merriweather",Georgia,serif;font-weight:400;font-size:23px;color:var(--white);margin-bottom:18px}
.foot-col li{list-style:none;font-size:13px;font-weight:700;color:var(--white);line-height:28px}
</style>
</head>
<body>

<!-- hero -->
<section class="abs hero">
  <div class="abs hero-photo" role="img" aria-label="Businessman in a suit using a tablet computer"></div>
  <div class="abs hero-panel"></div>
  <div class="abs social" aria-label="Social links"><span></span><span></span><span></span><span></span></div>
  <div class="abs phone">
    <svg width="14" height="14" viewBox="0 0 24 24"><path fill="#fff" d="M6.6 10.8a15 15 0 0 0 6.6 6.6l2.2-2.2c.3-.3.7-.4 1-.2 1.1.4 2.3.6 3.6.6.6 0 1 .4 1 1V20c0 .6-.4 1-1 1A17 17 0 0 1 3 4c0-.6.4-1 1-1h3.5c.6 0 1 .4 1 1 0 1.3.2 2.5.6 3.6.1.3 0 .7-.2 1z"/></svg>
    +1 555 014 2288
  </div>
  <div class="abs brand"><i></i>brindlecove.com</div>
  <nav class="abs nav">
    <a class="current" href="#">Home</a><a href="#">About Me</a><a href="#">Financial Planning</a><a href="#">Investment Help</a><a href="#">Advice</a><a href="#">Contacts</a>
  </nav>
  <a class="abs pill cta-top" href="#">Free Consultation</a>
  <h1 class="abs hero-title serif">Because Money Doesn't Come With Instructions</h1>
  <p class="abs hero-lead">Sure, dealing with your finances can be intimidating.</p>
  <p class="abs hero-text">That's why we take the time to listen to you, learn your goals and then create your plan using Adam Kerrow's philosophies that reflect the latest academic research.</p>
</section>

<!-- services -->
<div class="abs service" style="left:50px">
  <span class="rule"></span>
  <h3>Saving Solutions</h3>
  <p>There is a variety of saving plans which can be tailored to your needs, including:<br><br>Tax Exempt Savings<br>Regular Savings..</p>
  <a class="pill" href="#">LEARN MORE</a>
</div>
<div class="abs service" style="left:425px">
  <span class="rule"></span>
  <h3>Tax Planning</h3>
  <p>Inheritance tax planning is an important element of your wealth management strategy, as it allows you to continue to help your loved ones after you're gone.</p>
  <a class="pill" href="#">LEARN MORE</a>
</div>
<div class="abs service" style="left:800px">
  <span class="rule"></span>
  <h3>University Fee Planning</h3>
  <p>We all want our children to have good prospects, which is why education fees planning is a vital wealth management matter that shouldn't be overlooked.</p>
  <a class="pill" href="#">LEARN MORE</a>
</div>
<div class="abs divider" style="top:1298px"></div>

<!-- about -->
<h2 class="abs about-title serif">About</h2>
<p class="abs about-intro">I am Adam Kerrow, a senior advisor for an independently owned financial planning company called Harbor Ledger.</p>
<p class="abs about-text">Harbor Ledger is an International Financial Planning company with offices in multiple jurisdictions over the world. Working with Harbor Ledger gives me the ability to advise international expatriates living in the middle east from where I live in USA.</p>
<a class="abs explore" href="#">EXPLORE MORE</a>
<div class="abs frame-back" role="img" aria-label="Hands typing on a laptop keyboard"></div>
<div class="abs frame-front"><div role="img" aria-label="Young couple looking at a laptop together"></div></div>
<div class="abs divider" style="top:1940px"></div>

<!-- testimonials -->
<h2 class="abs testi-title serif">Testimonials</h2>
<p class="abs testi-sub">Read what my clients say about my level of service and the success that they've achieved</p>
<div class="abs arrows">
  <svg width="22" height="14" viewBox="0 0 22 14"><path d="M8 1 2 7l6 6M2 7h19" fill="none" stroke="#c8c8c8" stroke-width="1.5"/></svg>
  <svg width="22" height="14" viewBox="0 0 22 14"><path d="M14 1l6 6-6 6M20 7H1" fill="none" stroke="#c8c8c8" stroke-width="1.5"/></svg>
</div>
<div class="abs quote" style="left:50px">
  <span class="mark">&ldquo;</span>
  <p>It is not every day that you come across a passionate and trustworthy financial advisor. Adam has encompassed that really well and has provided us with the helping hand to dream that much more and make that dream a possible reality. Thanks Adam!</p>
  <span class="who">Hale M.J.</span><span class="role">Director of "Market Weekly"</span>
</div>
<div class="abs quote" style="left:428px">
  <span class="mark">&ldquo;</span>
  <p>In just 2 very short meetings with Adam he managed to find the solution personally catered to my situation and expectations. Punctual, well informed and very reliable.</p>
  <span class="who">Carter T.M.</span><span class="role">Director at Norvane Solutions Ltd</span>
</div>
<div class="abs quote" style="left:808px">
  <span class="mark">&ldquo;</span>
  <p>A very professional financial advisor, who is true to his word. Adam has demonstrated a high amount of integrity in the time I have known him, and he is fast to respond to my concerns. I feel that Adam is genuinely putting my financial gains before his own, a quality that comforts me in my investments.</p>
  <span class="who">Winter J.R.</span><span class="role">Managing Director of KDL Global</span>
</div>
<div class="abs divider" style="top:2490px"></div>

<!-- philosophy -->
<div class="abs band"></div>
<h2 class="abs philo-title serif">More Than 100 Financial Planners,One Philosophy</h2>
<div class="abs video" role="img" aria-label="Video still of a hand signing a document on a desk"></div>
<svg class="abs play" width="44" height="48" viewBox="0 0 44 48"><path d="M4 2l38 22L4 46z" fill="#fff"/></svg>
<p class="abs philo-lead">Every single one of our financial advisors receives rigorous training in Paul Ardenne's philosophy, which is based on academic research <span>(including that of a Nobel laureate in Economics)</span> and Behavioral Finance.</p>
<p class="abs philo-text">All of our planners believe that everyone, rich or not so rich, deserves great financial advice and planning services. No matter which advisor you work with, you can be confident that they'll put YOUR BEST INTERESTS FIRST and that you are getting the best experience we have to offer.</p>
<a class="abs pill cta-analysis" href="#">Get Your Free Financial Analysis</a>

<!-- signup & contact -->
<section class="abs connect"></section>
<svg class="abs" style="left:50px;top:3652px" width="38" height="34" viewBox="0 0 38 34"><path d="M2 15 36 2 30 32 18 22 14 31 13 20 2 15z M13 20 36 2" fill="none" stroke="#fff" stroke-width="2" stroke-linejoin="round"/></svg>
<h2 class="abs block-title" style="left:116px;top:3642px">Sign Up</h2>
<p class="abs signup-note">Get subscriber only insights &amp; news delivered by Adam Kerrow</p>
<div class="abs email-field">Enter Your E-mail</div>
<a class="abs pill submit" href="#">Submit</a>

<svg class="abs" style="left:614px;top:3656px" width="36" height="28" viewBox="0 0 36 28"><rect x="1.5" y="1.5" width="33" height="25" rx="2" fill="none" stroke="#fff" stroke-width="2.5"/><path d="M2 3l16 13L34 3" fill="none" stroke="#fff" stroke-width="2.5"/></svg>
<h2 class="abs block-title" style="left:670px;top:3642px">Contact Me</h2>
<dl class="abs contact-row" style="top:3708px"><dt>E-mail</dt><dd>hello@brindlecove.com</dd></dl>
<dl class="abs contact-row" style="top:3752px"><dt>Telephone</dt><dd>+1 555 014 2288</dd></dl>
<dl class="abs contact-row" style="top:3795px"><dt>Adress</dt><dd>48 Orchard Row, Ste. 12 Millbrook, NY 10501</dd></dl>

<!-- footer -->
<footer class="abs footer"></footer>
<div class="abs fine">
  <p>Investment products and services are offered only to residents of the states listed on our disclosure page. Advisory services are provided through Harbor Ledger, a registered investment adviser. Securities are offered through an independent member broker. Please review all materials before acting.</p>
  <p>All other trademarks and copyrights are the property of their respective holders. This website provides general information only and does not give legal or tax advice.</p>
</div>
<div class="abs copyright">COPYRIGHT © 2016</div>
<div class="abs foot-col" style="left:628px;top:3940px">
  <h4>Financial Planning</h4>
  <ul><li>Investment Management</li><li>Retirement Planning</li><li>Long Term Care</li><li>Estate Planning</li><li>Social Security</li></ul>
</div>
<div class="abs foot-col" style="left:900px;top:3940px">
  <h4>Investment Help</h4>
  <ul><li>Wealth Management</li><li>Retirement &amp; College</li><li>Savings Business Owners</li><li>Insurance &amp; Annuities</li><li>Cash &amp; Credit</li><li>Stocks, Bonds &amp; Mutual Funds</li></ul>
</div>

</body>
</html>
```